Billboard design for a new container self storage

I’m after a sign designing for a new container storage opening. located in the heart of Scunthorpe. Open 24/7. Brand new containers. On site security. Best prices guaranteed

Open 24/7
Safe secure self storage
Best prices Guaranteed
Site address
Tarbury Row
Scunthorpe
ZX48 2QT
Also include next left and an arrow
Dark green/ grey and fluorescent lime green

Contact - info@marshvaleunits.co.uk
07946201583

Website colours attached

Requirements
Must have
• Instagram logo @Marshvaleselfstorage

```html
<!DOCTYPE html>
<html lang="en">
<head>
<meta charset="utf-8">
<title>Safe Secure Self Storage – Billboard</title>
<link rel="stylesheet" href="https://fonts.googleapis.com/css2?family=Anton&family=Bebas+Neue&family=Michroma&display=swap">
<style>
  :root {
    --page: #ffffff;
    --board-dark: #333335;
    --board-light: #4a4a4c;
    --lime: #8cc63f;
    --lime-light: #a9d65a;
    --headline-top: #95c950;
    --headline-bottom: #dde766;
    --ink: #2c2c2e;
    --white: #ffffff;
  }
  * { margin: 0; padding: 0; box-sizing: border-box; }
  html, body {
    width: 800px;
    height: 1200px;
    overflow: hidden;
    background: var(--page);
  }
  .billboard {
    position: absolute;
    left: 40px;
    top: 420px;
    width: 720px;
    height: 360px;
  }
  .billboard svg { display: block; width: 720px; height: 360px; }
  .tag-text { font-family: "Michroma", sans-serif; font-size: 17px; fill: var(--ink); }
  .headline { font-family: "Anton", sans-serif; font-size: 95px; }
  .band-text { font-family: "Anton", sans-serif; font-size: 44px; fill: var(--ink); }
  .address { font-family: "Bebas Neue", sans-serif; font-size: 26px; fill: var(--white); }
  .contact { font-family: "Bebas Neue", sans-serif; font-size: 23px; fill: var(--headline-bottom); }
</style>
</head>
<body>
<main class="billboard">
  <svg viewBox="0 0 720 360" xmlns="http://www.w3.org/2000/svg">
    <defs>
      <radialGradient id="board-glow" cx="50%" cy="50%" r="60%">
        <stop offset="0" stop-color="var(--board-light)"/>
        <stop offset="1" stop-color="var(--board-dark)"/>
      </radialGradient>
      <linearGradient id="headline-split-one" gradientUnits="userSpaceOnUse" x1="0" y1="49" x2="0" y2="135">
        <stop offset="0.48" stop-color="var(--headline-top)"/>
        <stop offset="0.48" stop-color="var(--headline-bottom)"/>
      </linearGradient>
      <linearGradient id="headline-split-two" gradientUnits="userSpaceOnUse" x1="0" y1="137" x2="0" y2="223">
        <stop offset="0.48" stop-color="var(--headline-top)"/>
        <stop offset="0.48" stop-color="var(--headline-bottom)"/>
      </linearGradient>
      <radialGradient id="band-glow" cx="50%" cy="50%" r="55%">
        <stop offset="0" stop-color="var(--lime-light)"/>
        <stop offset="1" stop-color="var(--lime)"/>
      </radialGradient>
    </defs>

    <rect class="board" width="720" height="360" fill="url(#board-glow)"/>

    <g class="opening-tag">
      <rect x="250" y="20" width="220" height="25" fill="var(--lime)"/>
      <circle cx="261" cy="32.5" r="3.5" fill="var(--board-light)" stroke="var(--white)" stroke-width="1.8"/>
      <circle cx="459" cy="32.5" r="3.5" fill="var(--board-light)" stroke="var(--white)" stroke-width="1.8"/>
      <text class="tag-text" x="274" y="40" textLength="172" lengthAdjust="spacingAndGlyphs">Open 24/7</text>
    </g>

    <g class="headline-group">
      <text class="headline" x="118" y="135" textLength="486" lengthAdjust="spacingAndGlyphs" fill="url(#headline-split-one)">SAFE SECURE</text>
      <text class="headline" x="97" y="223" textLength="528" lengthAdjust="spacingAndGlyphs" fill="url(#headline-split-two)">SELF STORAGE</text>
    </g>

    <g class="price-band">
      <rect x="88" y="226" width="544" height="59" fill="url(#band-glow)"/>
      <text class="band-text" x="110" y="275" textLength="500" lengthAdjust="spacingAndGlyphs">BEST PRICES GUARANTEED</text>
    </g>

    <g class="address-line">
      <path class="pin-icon" d="M96 292a8 8 0 0 0-8 8c0 6 8 13 8 13s8-7 8-13a8 8 0 0 0-8-8zm0 4.5a3.5 3.5 0 1 1 0 7 3.5 3.5 0 0 1 0-7z" fill="var(--lime)" fill-rule="evenodd"/>
      <text class="address" x="109" y="312" textLength="458" lengthAdjust="spacingAndGlyphs">TARBURY ROW, SCUNTHORPE, ZX48 2QT (NEXT LEFT)</text>
      <g class="arrow-icon" stroke="var(--white)" stroke-width="2" fill="none">
        <line x1="572" y1="303" x2="608" y2="303"/>
        <polyline points="602,298 608,303 602,308"/>
      </g>
    </g>

    <g class="contact-line">
      <g class="mail-icon" stroke="var(--white)" stroke-width="1.3" fill="none">
        <rect x="120" y="325" width="23" height="14"/>
        <polyline points="120,325 131.5,334 143,325"/>
        <line x1="120" y1="339" x2="128" y2="331"/>
        <line x1="143" y1="339" x2="135" y2="331"/>
      </g>
      <text class="contact" x="148" y="340" textLength="272" lengthAdjust="spacingAndGlyphs">INFO@MARSHVALEUNITS.CO.UK</text>
      <path class="phone-icon" d="M433 325c2-1 3 0 4 2l1 3c0 1-1 2-2 2 1 2 3 4 5 5 0-1 1-2 2-2l3 1c2 1 2 2 1 4-1 1-2 2-4 1-5-2-9-6-11-11-0.5-2 0-4 1-5z" fill="var(--white)"/>
      <text class="contact" x="452" y="340" textLength="114" lengthAdjust="spacingAndGlyphs">07946201583</text>
    </g>
  </svg>
</main>
</body>
</html>
```